Four in One (Flexible infographic for Content Management Industry)

See attachment.
A graphic depicting 4 products, where each can stand on its own and each can be combined with others, but where, if all are taken together, the best result is achieved (the "super product").
Intended use is web. See attached file as an example.
The most basic idea is as the attached diagram shows, where 4 rectangles are arranged in a quadrangle, with a middle rectangle in the center representing the combined 4 products. This concept is fine except it is a bit too obvious as it stands. We are looking for either a variation of this or another concept.
The audience is technical + professional + enterprise - NOT consumers. Hence the design should be conservative in nature.
We are aware of tools like as Canva or Pictogram where such graphics are available, but we are looking for something with a bit more imagination and flexibility.
This graphic should be targeted to web sites and be delivered with vector-based (SVG) graphics.

```html
<!DOCTYPE html>
<html lang="en">
<head>
<meta charset="utf-8">
<title>Four in One – Super Product</title>
<link rel="stylesheet" href="https://fonts.googleapis.com/css2?family=Figtree:wght@400;500;600;700;800&display=swap">
<style>
  :root {
    --navy: #172b66;
    --teal: #22ddd2;
    --blue: #2f74e8;
    --purple: #8b17e8;
    --ink: #132a4a;
    --text: #1b1f2a;
    --rule: #8a8f99;
    --divider: #d6d8dd;
    --ring: #dedfe2;
    --button: #f0f0f3;
    --white: #ffffff;
  }
  * { box-sizing: border-box; margin: 0; padding: 0; }
  html, body { width: 1200px; height: 900px; overflow: hidden; background: var(--white); }
  body { font-family: "Figtree", "Segoe UI", sans-serif; color: var(--text); }
  .canvas { position: relative; width: 1200px; height: 900px; overflow: hidden; }

  .hub-diagram { position: absolute; left: 0; top: 0; width: 1200px; height: 412.5px; }
  .hub-title { font-family: "Figtree", sans-serif; font-weight: 700; font-size: 25px; fill: var(--ink); letter-spacing: 0.3px; }

  .product-columns { position: absolute; left: 8px; top: 452px; display: flex; }
  .product-column { width: 296px; height: 413px; padding-left: 27px; }
  .product-column + .product-column { border-left: 1px solid var(--divider); }

  .product-header { font-size: 21px; font-weight: 700; line-height: 26px; }
  .product-column.navy .product-header { color: var(--ink); }
  .product-column.teal .product-header { color: var(--teal); }
  .product-column.blue .product-header { color: var(--blue); }
  .product-column.purple .product-header { color: var(--purple); }

  .product-summary { margin-top: 2px; width: 230px; font-size: 16px; font-weight: 500; line-height: 21px; color: var(--text); }
  .product-rule { margin-top: 29px; width: 241px; height: 1px; background: var(--rule); border: 0; }

  .feature-list { list-style: none; margin-top: 16px; }
  .feature-item { display: flex; align-items: center; height: 37px; font-size: 14px; font-weight: 500; color: var(--text); word-spacing: 1px; }
  .feature-item svg { width: 17px; height: 17px; margin-right: 12px; flex: none; }

  .learn-more { display: flex; align-items: center; justify-content: center; margin-top: 50px; width: 192px; height: 35px; border-radius: 18px; background: var(--button); color: var(--ink); font-size: 13.5px; font-weight: 800; letter-spacing: 2.4px; text-decoration: none; }
</style>
</head>
<body>
<main class="canvas">

  <svg class="hub-diagram" viewBox="0 0 960 330" aria-label="Four products combining into one super product">
    <defs>
      <filter id="hub-shadow" x="-20%" y="-20%" width="140%" height="140%">
        <feDropShadow dx="0" dy="2" stdDeviation="3" flood-color="#000" flood-opacity="0.18"/>
      </filter>
    </defs>

    <circle class="outer-ring" cx="480" cy="0" r="313" fill="none" stroke="var(--ring)" stroke-width="2"/>

    <g class="segments" stroke="var(--white)" stroke-width="3" stroke-linejoin="round">
      <path fill="var(--navy)" d="M210 0 A270 270 0 0 0 289.1 190.9 L373.9 106.1 A150 150 0 0 1 330 0 Z"/>
      <path fill="var(--teal)" d="M289.1 190.9 A270 270 0 0 0 480 270 L480 150 A150 150 0 0 1 373.9 106.1 Z"/>
      <path fill="var(--blue)" d="M480 270 A270 270 0 0 0 670.9 190.9 L586.1 106.1 A150 150 0 0 1 480 150 Z"/>
      <path fill="var(--purple)" d="M670.9 190.9 A270 270 0 0 0 750 0 L630 0 A150 150 0 0 1 586.1 106.1 Z"/>
    </g>

    <circle class="hub" cx="480" cy="0" r="111" fill="var(--white)" stroke="#e6e7ea" stroke-width="1" filter="url(#hub-shadow)"/>
    <text class="hub-title" x="480" y="43" text-anchor="middle">SUPER</text>
    <text class="hub-title" x="480" y="72" text-anchor="middle">PRODUCT</text>

    <g class="ring-markers">
      <circle cx="183" cy="104" r="16" fill="var(--navy)" opacity="0.5"/>
      <circle cx="183" cy="104" r="10" fill="var(--navy)"/>
      <circle cx="364" cy="292" r="16" fill="var(--teal)" opacity="0.3"/>
      <circle cx="364" cy="292" r="10" fill="var(--teal)"/>
      <circle cx="595" cy="292" r="16" fill="var(--blue)" opacity="0.5"/>
      <circle cx="595" cy="292" r="10" fill="var(--blue)"/>
      <circle cx="777" cy="104" r="16" fill="var(--purple)" opacity="0.45"/>
      <circle cx="777" cy="104" r="10" fill="var(--purple)"/>
    </g>

    <g class="icon-cloud" fill="var(--white)">
      <path d="M264 82 a9 9 0 0 1 2 -17.5 a12 12 0 0 1 22.5 -2 a9 9 0 0 1 6 6 H288 a13 13 0 0 0 -10 13.5 Z"/>
      <circle cx="292" cy="82" r="13" fill="var(--white)" stroke="var(--navy)" stroke-width="2.5"/>
      <path d="M286.5 82 l4 4 l7 -7.5" fill="none" stroke="var(--navy)" stroke-width="2.6" stroke-linecap="round" stroke-linejoin="round"/>
    </g>

    <g class="icon-layers" fill="none" stroke="var(--white)" stroke-width="2.6" stroke-linejoin="round" stroke-linecap="round">
      <path d="M397 171 L420 183 L397 195 L374 183 Z"/>
      <path d="M389 184 L397 179 L405 184"/>
      <path d="M374 192 L397 204 L420 192"/>
      <path d="M374 201 L397 213 L420 201"/>
    </g>

    <g class="icon-apps" fill="var(--white)">
      <rect x="537" y="173" width="18" height="18" rx="3.5"/>
      <rect x="537" y="196" width="18" height="18" rx="3.5"/>
      <rect x="560" y="196" width="18" height="18" rx="3.5"/>
      <rect x="560.5" y="173.5" width="16" height="16" rx="3.5" transform="rotate(45 568.5 181.5)"/>
    </g>

    <g class="icon-document">
      <path d="M662 52 H690 a4 4 0 0 1 4 4 V84 L684 96 H662 a4 4 0 0 1 -4 -4 V56 a4 4 0 0 1 4 -4 Z" fill="var(--white)"/>
      <path d="M684 96 V88 a2 2 0 0 1 2 -2 H694" fill="none" stroke="var(--purple)" stroke-width="2.2"/>
      <g stroke="var(--purple)" stroke-width="3" stroke-linecap="round">
        <line x1="666" y1="63" x2="686" y2="63"/>
        <line x1="666" y1="71" x2="682" y2="71"/>
        <line x1="666" y1="79" x2="676" y2="79"/>
      </g>
    </g>
  </svg>

  <section class="product-columns">
    <article class="product-column navy">
      <h2 class="product-header">Header Text Here</h2>
      <p class="product-summary">Lorem ipsum dolor sit amet, consectetur adipiscing elit, sed do eiusmod tempor incididunt ut labore et dolore magna aliqua.</p>
      <hr class="product-rule">
      <ul class="feature-list">
        <li class="feature-item"><svg viewBox="0 0 16 16"><circle cx="8" cy="8" r="7" fill="none" stroke="var(--navy)" stroke-width="1.3"/><path d="M5 8.2l2 2 4-4.2" fill="none" stroke="var(--navy)" stroke-width="1.4" stroke-linecap="round" stroke-linejoin="round"/></svg>Insert bullet text here</li>
        <li class="feature-item"><svg viewBox="0 0 16 16"><circle cx="8" cy="8" r="7" fill="none" stroke="var(--navy)" stroke-width="1.3"/><path d="M5 8.2l2 2 4-4.2" fill="none" stroke="var(--navy)" stroke-width="1.4" stroke-linecap="round" stroke-linejoin="round"/></svg>Insert bullet text here</li>
        <li class="feature-item"><svg viewBox="0 0 16 16"><circle cx="8" cy="8" r="7" fill="none" stroke="var(--navy)" stroke-width="1.3"/><path d="M5 8.2l2 2 4-4.2" fill="none" stroke="var(--navy)" stroke-width="1.4" stroke-linecap="round" stroke-linejoin="round"/></svg>Insert bullet text here</li>
        <li class="feature-item"><svg viewBox="0 0 16 16"><circle cx="8" cy="8" r="7" fill="none" stroke="var(--navy)" stroke-width="1.3"/><path d="M5 8.2l2 2 4-4.2" fill="none" stroke="var(--navy)" stroke-width="1.4" stroke-linecap="round" stroke-linejoin="round"/></svg>Insert bullet text here</li>
      </ul>
      <a class="learn-more" href="#">LEARN MORE</a>
    </article>

    <article class="product-column teal">
      <h2 class="product-header">Header Text Here</h2>
      <p class="product-summary">Lorem ipsum dolor sit amet, consectetur adipiscing elit, sed do eiusmod tempor incididunt ut labore et dolore magna aliqua.</p>
      <hr class="product-rule">
      <ul class="feature-list">
        <li class="feature-item"><svg viewBox="0 0 16 16"><circle cx="8" cy="8" r="7" fill="none" stroke="var(--navy)" stroke-width="1.3"/><path d="M5 8.2l2 2 4-4.2" fill="none" stroke="var(--navy)" stroke-width="1.4" stroke-linecap="round" stroke-linejoin="round"/></svg>Insert bullet text here</li>
        <li class="feature-item"><svg viewBox="0 0 16 16"><circle cx="8" cy="8" r="7" fill="none" stroke="var(--navy)" stroke-width="1.3"/><path d="M5 8.2l2 2 4-4.2" fill="none" stroke="var(--navy)" stroke-width="1.4" stroke-linecap="round" stroke-linejoin="round"/></svg>Insert bullet text here</li>
        <li class="feature-item"><svg viewBox="0 0 16 16"><circle cx="8" cy="8" r="7" fill="none" stroke="var(--navy)" stroke-width="1.3"/><path d="M5 8.2l2 2 4-4.2" fill="none" stroke="var(--navy)" stroke-width="1.4" stroke-linecap="round" stroke-linejoin="round"/></svg>Insert bullet text here</li>
        <li class="feature-item"><svg viewBox="0 0 16 16"><circle cx="8" cy="8" r="7" fill="none" stroke="var(--navy)" stroke-width="1.3"/><path d="M5 8.2l2 2 4-4.2" fill="none" stroke="var(--navy)" stroke-width="1.4" stroke-linecap="round" stroke-linejoin="round"/></svg>Insert bullet text here</li>
      </ul>
      <a class="learn-more" href="#">LEARN MORE</a>
    </article>

    <article class="product-column blue">
      <h2 class="product-header">Header Text Here</h2>
      <p class="product-summary">Lorem ipsum dolor sit amet, consectetur adipiscing elit, sed do eiusmod tempor incididunt ut labore et dolore magna aliqua.</p>
      <hr class="product-rule">
      <ul class="feature-list">
        <li class="feature-item"><svg viewBox="0 0 16 16"><circle cx="8" cy="8" r="7" fill="none" stroke="var(--navy)" stroke-width="1.3"/><path d="M5 8.2l2 2 4-4.2" fill="none" stroke="var(--navy)" stroke-width="1.4" stroke-linecap="round" stroke-linejoin="round"/></svg>Insert bullet text here</li>
        <li class="feature-item"><svg viewBox="0 0 16 16"><circle cx="8" cy="8" r="7" fill="none" stroke="var(--navy)" stroke-width="1.3"/><path d="M5 8.2l2 2 4-4.2" fill="none" stroke="var(--navy)" stroke-width="1.4" stroke-linecap="round" stroke-linejoin="round"/></svg>Insert bullet text here</li>
        <li class="feature-item"><svg viewBox="0 0 16 16"><circle cx="8" cy="8" r="7" fill="none" stroke="var(--navy)" stroke-width="1.3"/><path d="M5 8.2l2 2 4-4.2" fill="none" stroke="var(--navy)" stroke-width="1.4" stroke-linecap="round" stroke-linejoin="round"/></svg>Insert bullet text here</li>
        <li class="feature-item"><svg viewBox="0 0 16 16"><circle cx="8" cy="8" r="7" fill="none" stroke="var(--navy)" stroke-width="1.3"/><path d="M5 8.2l2 2 4-4.2" fill="none" stroke="var(--navy)" stroke-width="1.4" stroke-linecap="round" stroke-linejoin="round"/></svg>Insert bullet text here</li>
      </ul>
      <a class="learn-more" href="#">LEARN MORE</a>
    </article>

    <article class="product-column purple">
      <h2 class="product-header">Header Text Here</h2>
      <p class="product-summary">Lorem ipsum dolor sit amet, consectetur adipiscing elit, sed do eiusmod tempor incididunt ut labore et dolore magna aliqua.</p>
      <hr class="product-rule">
      <ul class="feature-list">
        <li class="feature-item"><svg viewBox="0 0 16 16"><circle cx="8" cy="8" r="7" fill="none" stroke="var(--navy)" stroke-width="1.3"/><path d="M5 8.2l2 2 4-4.2" fill="none" stroke="var(--navy)" stroke-width="1.4" stroke-linecap="round" stroke-linejoin="round"/></svg>Insert bullet text here</li>
        <li class="feature-item"><svg viewBox="0 0 16 16"><circle cx="8" cy="8" r="7" fill="none" stroke="var(--navy)" stroke-width="1.3"/><path d="M5 8.2l2 2 4-4.2" fill="none" stroke="var(--navy)" stroke-width="1.4" stroke-linecap="round" stroke-linejoin="round"/></svg>Insert bullet text here</li>
        <li class="feature-item"><svg viewBox="0 0 16 16"><circle cx="8" cy="8" r="7" fill="none" stroke="var(--navy)" stroke-width="1.3"/><path d="M5 8.2l2 2 4-4.2" fill="none" stroke="var(--navy)" stroke-width="1.4" stroke-linecap="round" stroke-linejoin="round"/></svg>Insert bullet text here</li>
        <li class="feature-item"><svg viewBox="0 0 16 16"><circle cx="8" cy="8" r="7" fill="none" stroke="var(--navy)" stroke-width="1.3"/><path d="M5 8.2l2 2 4-4.2" fill="none" stroke="var(--navy)" stroke-width="1.4" stroke-linecap="round" stroke-linejoin="round"/></svg>Insert bullet text here</li>
      </ul>
      <a class="learn-more" href="#">LEARN MORE</a>
    </article>
  </section>

</main>
</body>
</html>
```